Global software company seeking new website design

Our existing website no longer meets our needs. We are seeking to develop a new website in Wordpress and need the look/feel, navigation and graphics designed to best effect. An overview of our company, and a brief on the functionality/key messaging of the website is in the attached PDF

Industry/Entity Type

Software

```html
<!DOCTYPE html>
<html lang="en">
<head>
<meta charset="utf-8">
<title>Veltrio Soft – Total Mailbox Migration</title>
<link rel="stylesheet" href="https://fonts.googleapis.com/css2?family=Open+Sans:wght@400;600;700&display=swap">
<style>
:root{
  --blue:#3f64b0;
  --card-blue:#4769b2;
  --purple:#574a9c;
  --orange:#f6a11b;
  --ink:#111;
  --body:#333;
  --white:#fff;
  --line:#e5e5e5;
}
*{box-sizing:border-box;margin:0;padding:0}
html,body{width:1200px;height:2812px;overflow:hidden}
body{position:relative;font-family:"Open Sans",Arial,sans-serif;color:var(--body);background:var(--white)}
.abs{position:absolute}
a{color:inherit;text-decoration:none}

/* header */
.site-header{left:0;top:0;width:1200px;height:112px;background:var(--white)}
.brand{left:210px;top:36px;display:flex;align-items:center;gap:10px}
.brand-mark{width:18px;height:18px;background:var(--blue)}
.brand-name{font-size:26px;font-weight:600;color:var(--blue);letter-spacing:.5px}
.brand-tag{left:239px;top:68px;font-size:13px;color:#444}
.top-bar{left:610px;top:18px;height:22px;display:flex;align-items:center}
.social{display:flex;gap:8px;margin-right:18px}
.social span{width:14px;height:14px;border-radius:50%;background:#888;display:block}
.call{font-size:16px;color:var(--ink);margin-right:18px}
.signin{width:72px;height:22px;background:var(--orange);color:var(--white);font-size:12px;display:flex;align-items:center;justify-content:center;margin-right:4px}
.search{width:22px;height:22px;border:1px solid var(--line);display:flex;align-items:center;justify-content:center}
.main-nav{left:0;top:56px;height:38px}
.main-nav a{position:absolute;top:0;height:38px;line-height:38px;font-size:14px;color:#444;white-space:nowrap}
.main-nav a.active{background:var(--blue);color:var(--white);padding:0 10px}
.dropdown{left:583px;top:94px;width:109px;height:155px;background:var(--purple);padding-top:10px}
.dropdown a{display:block;color:var(--white);font-size:11px;padding-left:10px;height:27px;line-height:27px;white-space:nowrap}

/* hero */
.hero{left:0;top:112px;width:1200px;height:452px;background:linear-gradient(100deg,#e6ebf0 0%,#f3f5f7 30%,#cfdbe6 65%,#9fbcd6 100%)}
.hero-copy{left:208px;top:134px;width:380px}
.hero-title{font-size:29px;font-weight:700;color:var(--blue);line-height:38px;white-space:nowrap}
.hero-text{font-size:15px;color:var(--ink);line-height:19px;margin-top:2px;width:356px}
.btn-cta{display:block;margin-top:12px;width:165px;height:36px;background:var(--orange);color:var(--white);font-size:15px;text-align:center;line-height:36px}
.dots{left:210px;top:509px;display:flex;gap:3px}
.dots span{width:11px;height:11px;background:#c9cdd3}
.dots span.on{background:var(--blue)}
.slide-arrow{top:262px;width:20px;height:40px;background:rgba(200,200,200,.7)}
.slide-arrow.left{left:0;border-radius:0 20px 20px 0}
.slide-arrow.right{right:0;border-radius:20px 0 0 20px}

.get-in-touch{left:0;top:651px;width:36px;height:125px;background:var(--orange);display:flex;align-items:center;justify-content:center}
.get-in-touch span{transform:rotate(-90deg);white-space:nowrap;color:var(--white);font-size:13px}

/* sections */
.section-title{left:0;width:1200px;text-align:center;font-size:29px;font-weight:700;color:var(--ink)}
.section-sub{left:0;width:1200px;text-align:center;font-size:15px;color:var(--ink)}

.service-card{top:739px;width:383px;height:287px;color:var(--white);text-align:center}
.service-card.technical{left:210px;background:var(--card-blue)}
.service-card.business{left:608px;background:var(--purple)}
.service-card svg{position:absolute;left:160px;top:40px}
.service-card h3{position:absolute;top:116px;width:100%;font-size:26px;font-weight:400}
.service-card p{position:absolute;top:156px;font-size:14px;line-height:18px}
.service-card.technical p{left:70px;width:243px}
.service-card.business p{left:60px;width:263px}
.btn-small{position:absolute;width:92px;height:22px;background:var(--orange);color:var(--white);font-size:11px;line-height:22px;text-align:center}
.service-card .btn-small{left:145px;top:229px}

.video-main{left:210px;top:1238px;width:643px;height:455px;background:linear-gradient(90deg,#5b5f63 0%,#8c9095 40%,#a7abaf 100%)}
.video-thumb{left:861px;width:129px;height:103px}
.play{position:absolute;border-radius:50%;background:rgba(255,255,255,.85)}
.play::after{content:"";position:absolute;top:50%;left:54%;transform:translate(-50%,-50%);border-style:solid;border-color:transparent transparent transparent #555}
.video-main .play::after{border-width:13px 0 13px 20px}
.video-thumb .play::after{border-width:6px 0 6px 9px}

.visitor-band{left:0;top:1935px;width:1200px;height:709px;background:linear-gradient(170deg,#cfc8c0 0%,#dedcd8 40%,#c9ced3 70%,#b7bdc3 100%)}
.visitor-photo{width:308px;height:308px;border-radius:50%;border:6px solid var(--white)}
.visitor-text{width:300px;text-align:center;font-size:14px;line-height:18px;color:var(--white)}

.site-footer{left:0;top:2651px;width:1200px;height:161px;background:var(--purple);color:var(--white)}
.footer-call{left:210px;top:46px;font-size:12px;font-weight:700}
.footer-rule{left:210px;top:71px;width:156px;height:1px;background:rgba(255,255,255,.7)}
.footer-social{left:210px;top:85px;display:flex;gap:8px}
.footer-social span{width:14px;height:14px;border-radius:50%;background:var(--white);display:block}
.footer-nav a{position:absolute;top:46px;font-size:12px}
</style>
</head>
<body>

<header class="site-header abs">
  <div class="brand abs"><span class="brand-mark"></span><span class="brand-name">Veltrio Soft</span></div>
  <div class="brand-tag abs">...mail moved right</div>
  <div class="top-bar abs">
    <div class="social" aria-label="Social links"><span></span><span></span><span></span></div>
    <span class="call">Call us 24x7 : 1800 555 0142</span>
    <a class="signin" href="#">SIGNIN</a>
    <span class="search"><svg width="11" height="11" viewBox="0 0 12 12"><circle cx="5" cy="5" r="3.5" fill="none" stroke="#999" stroke-width="1.4"/><line x1="7.6" y1="7.6" x2="11" y2="11" stroke="#999" stroke-width="1.4"/></svg></span>
  </div>
  <nav class="main-nav abs">
    <a style="left:517px">Solutions</a>
    <a class="active" style="left:583px">Products</a>
    <a style="left:666px">Resources</a>
    <a style="left:746px">Partners</a>
    <a style="left:818px">Support</a>
    <a style="left:885px">Company</a>
    <a style="left:964px">Blog</a>
  </nav>
</header>

<section class="hero abs" role="img" aria-label="Photo of a hand touching a tablet showing charts beside a coffee cup">
  <div class="hero-copy abs">
    <h1 class="hero-title">Total Mailbox Migration</h1>
    <p class="hero-text">Lorem ipsum dolor sit amet, adipisicing elit, sed do eiusmod tempor incididunt ut et aliqua. Ut enim ad minim veniam,</p>
    <a class="btn-cta" href="#">Call to Action</a>
  </div>
  <div class="slide-arrow left abs"></div>
  <div class="slide-arrow right abs"></div>
</section>
<div class="dots abs"><span class="on"></span><span></span><span></span></div>

<nav class="dropdown abs">
  <a>Archive Ferry</a><a>Mailbox Ferry</a><a>PST Control Deck</a><a>Vault Storage</a><a>Mover Kit</a>
</nav>

<a class="get-in-touch abs" href="#"><span>Get in Touch</span></a>

<h2 class="section-title abs" style="top:632px">What we do</h2>
<p class="section-sub abs" style="top:676px">Lorem ipsum dolor sit amet, consectetur adipisicing elit, sed do eiusmod tempor incididunt</p>

<article class="service-card technical abs">
  <svg width="64" height="64" viewBox="0 0 64 64" fill="none" stroke="#fff" stroke-width="2">
    <path d="M10 54 L38 26"/><path d="M36 20a12 12 0 0 1 16-10l-7 7 2 5 5 2 7-7a12 12 0 0 1-10 16z"/>
    <path d="M54 54 L28 28"/><path d="M8 8l8 4 4 8-4 4-8-4-4-8z"/><path d="M50 50l6 6"/>
  </svg>
  <h3>Technical</h3>
  <p>Software that powers migration of email archives, Exchange and PST files</p>
  <a class="btn-small">Learn More</a>
</article>
<article class="service-card business abs">
  <svg width="64" height="64" viewBox="0 0 64 64" fill="none" stroke="#fff" stroke-width="2">
    <circle cx="32" cy="18" r="13"/><path d="M8 62c0-16 10-26 24-26s24 10 24 26"/><path d="M28 36l4 6 4-6M32 42l-4 12 4 6 4-6z"/>
  </svg>
  <h3>Business</h3>
  <p>Software that drive down the cost of email migration and delivers projects on time and on budget</p>
  <a class="btn-small">Learn More</a>
</article>

<h2 class="section-title abs" style="top:1135px">Our video listing</h2>
<p class="section-sub abs" style="top:1179px">Lorem ipsum dolor sit amet, consectetur adipisicing elit, sed do eiusmod tempor incididunt</p>

<div class="video-main abs" role="img" aria-label="Video still of a businessman in a suit holding a tablet">
  <span class="play" style="left:282px;top:188px;width:72px;height:72px"></span>
</div>
<div class="video-thumb abs" style="top:1238px;background:linear-gradient(135deg,#dbe6f0,#8fb2d4)" role="img" aria-label="Video still of hands with charts"><span class="play" style="left:50px;top:37px;width:30px;height:30px"></span></div>
<div class="video-thumb abs" style="top:1356px;background:linear-gradient(135deg,#e9ecef,#7c8088)" role="img" aria-label="Video still of a businessman with a tablet"><span class="play" style="left:50px;top:37px;width:30px;height:30px"></span></div>
<div class="video-thumb abs" style="top:1474px;background:linear-gradient(135deg,#b9c8d6,#4f6f8e)" role="img" aria-label="Video still of colleagues at computers"><span class="play" style="left:50px;top:37px;width:30px;height:30px"></span></div>
<div class="video-thumb abs" style="top:1590px;background:linear-gradient(135deg,#eef0f2,#a9a39c)" role="img" aria-label="Video still of a smiling team"><span class="play" style="left:50px;top:37px;width:30px;height:30px"></span></div>

<h2 class="section-title abs" style="top:1832px">Two types of visitor</h2>
<p class="section-sub abs" style="top:1876px">Lorem ipsum dolor sit amet, consectetur adipisicing elit, sed do eiusmod tempor incididunt</p>

<section class="visitor-band abs" role="img" aria-label="Blurred photo of hands typing on a keyboard"></section>
<div class="visitor-photo abs" style="left:259px;top:2118px;background:linear-gradient(160deg,#eef2f5,#9fb0c2)" role="img" aria-label="Photo of a man on the phone at a laptop"></div>
<div class="visitor-photo abs" style="left:634px;top:2118px;background:linear-gradient(160deg,#e2e6ea,#6f8aa6)" role="img" aria-label="Photo of hands using a tablet with charts"></div>
<p class="visitor-text abs" style="left:263px;top:2440px">Lorem ipsum dolor sit amet, consectetur adipisicing elit, sed do eiusmod tempor incididunt ut labore et dolore</p>
<p class="visitor-text abs" style="left:638px;top:2440px">Lorem ipsum dolor sit amet, consectetur adipisicing elit, sed do eiusmod tempor incididunt ut labore et dolore</p>
<a class="btn-small abs" style="left:367px;top:2512px">Learn More</a>
<a class="btn-small abs" style="left:742px;top:2512px">Learn More</a>

<footer class="site-footer abs">
  <div class="footer-call abs">Call us 24x7 : 1800 555 0142</div>
  <div class="footer-rule abs"></div>
  <div class="footer-social abs" aria-label="Social links"><span></span><span></span><span></span></div>
  <nav class="footer-nav">
    <a style="left:429px">Solutions</a><a style="left:500px">Products</a><a style="left:568px">Resources</a>
    <a style="left:645px">Partners</a><a style="left:711px">Support</a><a style="left:774px">Company</a><a style="left:847px">Blog</a>
    <a style="left:951px">© 2014</a>
  </nav>
</footer>

</body>
</html>
```